Bref créative
Cytovane Brochure
12 pages brochure
It's a 12 pages brochure about a molecular laboratory.
High tech project innovator and at the same time very reliable
Health
Doctors
Advanced concept but at the same time show professionalism
Attached is a brochure that was initiated but not finished by another designer.
cytovane logo

```html
<!DOCTYPE html>
<html lang="en">
<head>
<meta charset="utf-8">
<title>Nuvelcyte Brochure Spread</title>
<link href="https://fonts.googleapis.com/css2?family=Open+Sans:wght@300;400;600&display=swap" rel="stylesheet">
<style>
  :root {
    --paper: #ffffff;
    --text: #5b5b5b;
    --green: #5aa83c;
    --teal: #2f8f9a;
    --swirl-light: #f3f3f3;
    --swirl-mid: #dcdcdc;
    --photo-blue: #8fb6d6;
    --photo-deep: #3f6f98;
    --band-green: #7cb342;
    --band-orange: #f39c12;
    --band-blue: #3a8fd0;
    --band-red: #e0533c;
    --band-purple: #8e5aa8;
  }
  * { box-sizing: border-box; margin: 0; padding: 0; }
  html, body { width: 1200px; height: 780px; overflow: hidden; background: var(--paper); }
  body { font-family: "Open Sans", Arial, sans-serif; color: var(--text); }
  .spread { position: relative; width: 1200px; height: 780px; }
  .page { position: absolute; top: 0; width: 600px; height: 780px; overflow: hidden; }
  .page-left { left: 0; background: linear-gradient(160deg, var(--paper) 40%, var(--swirl-light) 70%, var(--paper) 90%); }
  .page-right { left: 600px; background: linear-gradient(200deg, var(--swirl-mid) 0%, var(--swirl-light) 35%, var(--paper) 60%); }
  .hero-photo {
    position: absolute; left: 0; top: 0; width: 600px; height: 318px;
    background: linear-gradient(90deg, var(--photo-deep) 0%, var(--photo-blue) 45%, rgba(255,255,255,0) 100%);
  }
  .mission { position: absolute; left: 295px; top: 328px; width: 298px; }
  .mission-title { font-weight: 300; font-size: 24px; line-height: 30px; color: var(--green); letter-spacing: 0.5px; margin-bottom: 2px; }
  .mission p { font-size: 9.6px; line-height: 16.6px; margin-bottom: 10px; text-align: justify; }
  .brand { position: absolute; left: 72px; top: 640px; }
  .brand-name { font-size: 30px; font-weight: 600; color: var(--teal); line-height: 36px; }
  .brand-tagline { font-size: 13px; font-weight: 600; color: var(--green); line-height: 18px; }
  .intro { position: absolute; left: 144px; top: 42px; width: 386px; }
  .intro p { font-size: 10px; line-height: 18px; margin-bottom: 18px; text-align: justify; }
  .lab-photo-top {
    position: absolute; left: 144px; top: 444px; width: 396px; height: 84px;
    background: linear-gradient(120deg, #5fb8e0 0%, #d8eef7 55%, #f0b74c 100%);
  }
  .lab-photo-bottom {
    position: absolute; left: 144px; top: 534px; width: 396px; height: 226px;
    background: linear-gradient(100deg, #b08a6a 0%, #e8dcd0 45%, #f2f2f2 100%);
  }
  .color-band { position: absolute; left: 0; bottom: 0; width: 1200px; height: 8px; display: flex; }
  .color-band span { flex: 1; }
  .spine { position: absolute; left: 599px; top: 0; width: 2px; height: 780px; background: linear-gradient(90deg, rgba(0,0,0,0.05), rgba(0,0,0,0)); }
</style>
</head>
<body>
<div class="spread">
  <section class="page page-left">
    <div class="hero-photo" role="img" aria-label="Photo of a lab scientist in mask and hair cap holding a test tube"></div>
    <div class="mission">
      <h2 class="mission-title">OUR MISSION</h2>
      <p>As a leader company in Personalized Medicine, we assist you in the screening, diagnosis, classification of cancer patients, and the optimization of drug therapy.</p>
      <p>Nuvelcyte, a CLIA-certified and CAP-accredited molecular laboratory, provides the highest quality molecular testing services to medical practitioners. Our highly experienced pathologists and molecular geneticists are leaders in their field with specialist knowledge and expertise. They provide current, informed and practical advice to assist with interpretation of results. Our pathologists are members of hospital boards and health policy committees and provide a renowned and comprehensive service to thousand patients each year, reaching private and public hospital beds, specialists and general practitioners throughout United States and worldwide. Doctors face an ever-expanding variety of genetic tests that could influence how they care for patients. Since the Human Genome Project was completed in 2003, the introduction of new genetic tests has far outpaced the ability of health practitioners<br>— who typically have little training in genetics<br>— to figure out what to do with them.</p>
    </div>
    <div class="brand">
      <div class="brand-name">Nuvelcyte</div>
      <div class="brand-tagline">Precision Ahead</div>
    </div>
  </section>

  <section class="page page-right">
    <div class="intro">
      <p>Nuvelcyte translates scientific discoveries into customized and more effective treatments for your patients. We can help to predict disease risk, or to determine how patients might respond to certain treatments.</p>
      <p>The technologies that come under the umbrella of molecular diagnostics at Nuvelcyte Laboratories include first-generation amplification, DNA probes, fluorescent in-situ hybridization (FISH), second-generation biochips, next-generation signal detection, biosensors and molecular labels, and gene expression profiling using microchips. The same technologies that are improving the discovery of therapeutic molecules for cancer, are been used by Nuvelcyte to assist in the screening, diagnosis, classification of cancer patients, and the optimization of drug therapy. Nuvelcyte is at the core of customized healthcare enabling providers to match drugs to patients based on their genetic profiles, to identify which health conditions an individual is susceptible to, and to determine how a given patient will respond to a particular therapy.</p>
    </div>
    <div class="lab-photo-top" role="img" aria-label="Photo of pipettes and colourful sample trays in a lab"></div>
    <div class="lab-photo-bottom" role="img" aria-label="Photo of a lab technician working at a bench with equipment"></div>
  </section>

  <div class="spine"></div>
  <div class="color-band">
    <span style="background:var(--band-green)"></span>
    <span style="background:var(--band-orange)"></span>
    <span style="background:var(--band-blue)"></span>
    <span style="background:var(--band-red)"></span>
    <span style="background:var(--band-purple)"></span>
    <span style="background:var(--band-green)"></span>
    <span style="background:var(--band-orange)"></span>
    <span style="background:var(--band-blue)"></span>
  </div>
</div>
</body>
</html>
```